Book Cover design: Waltz beside a Heron.

I need a front and back cover for my book called 'Waltz beside a Heron'.
It is self development book for help a person to be a better coach.
It is a metaphor. Dance is asking questions and the octopus is the person you are coaching (complex with my 'tentacles').
The audience would be adults. so want the cover to capture attention and also show that is have something of interest inside.
I have attach my first attempt. Please be bold.
The best sellers in this market place have simple but clear front page & back pages.

All the words are important but the sub-title is likely to change.

Target Market(s)

Adults who work with each other.
More business type people.

Industry/Entity Type

Leadership

Font styles to use
Serif

Requirements
Must have
• My project must have... The words that in the draft mock up.
• 'Waltz beside a Heron' [TITLE]
• 'A Map for Honest Mentoring'[SUB-TITLE]
• How to create inspiration and accountability using
• Five Critical Moments.[SUB_TITLE]
• By Godfrey T Haswell
Nice to have
• Clever and simple.

```html
<!DOCTYPE html>
<html lang="en">
<head>
<meta charset="utf-8">
<title>Waltz beside a Heron — Book Cover</title>
<link rel="stylesheet" href="https://fonts.googleapis.com/css2?family=Anton&family=Oswald:wght@300;500;700&display=swap">
<style>
  :root {
    --page-bg: #ffffff;
    --cover-white: #ffffff;
    --brand-red: #e01020;
    --brand-red-deep: #c10e1c;
    --rule-gold: #c9a94a;
    --panel-grey: #e4e4e4;
    --ink-dark: #1a1a1a;
    --ink-mid: #7a7a7a;
    --art-grey: #414045;
    --art-yellow: #f6c40c;
    --seal-gold: #e0a84a;
    --seal-gold-light: #f8e3a0;
    --seal-navy: #131a2c;
  }
  html, body {
    margin: 0;
    width: 1200px;
    height: 1200px;
    overflow: hidden;
    background: var(--page-bg);
  }
  .canvas {
    position: relative;
    width: 1200px;
    height: 1200px;
  }
  .book-cover {
    position: absolute;
    left: 152px;
    top: 20px;
    width: 896px;
    height: 1160px;
    box-shadow: 4px 6px 10px rgba(0,0,0,0.35);
    background: var(--cover-white);
  }
  .book-cover svg { display: block; }
  .author-name { font-family: 'Oswald', sans-serif; font-weight: 300; }
  .title-main { font-family: 'Anton', 'Oswald', sans-serif; }
  .title-link { font-family: 'Oswald', sans-serif; font-weight: 700; }
  .tagline { font-family: 'Oswald', sans-serif; font-weight: 700; }
  .seal-text { font-family: 'Oswald', sans-serif; font-weight: 700; }
</style>
</head>
<body>
<div class="canvas">
  <div class="book-cover">
    <svg width="896" height="1160" viewBox="0 0 896 1160" xmlns="http://www.w3.org/2000/svg">
      <defs>
        <linearGradient id="redBand" x1="0" y1="0" x2="0" y2="1">
          <stop offset="0" stop-color="var(--brand-red)"/>
          <stop offset="1" stop-color="var(--brand-red-deep)"/>
        </linearGradient>
        <linearGradient id="darkInk" x1="0" y1="0" x2="0" y2="1">
          <stop offset="0" stop-color="var(--ink-dark)"/>
          <stop offset="0.55" stop-color="var(--ink-dark)"/>
          <stop offset="1" stop-color="var(--ink-mid)"/>
        </linearGradient>
        <linearGradient id="artTones" x1="0" y1="0" x2="0" y2="1">
          <stop offset="0" stop-color="var(--art-yellow)"/>
          <stop offset="0.35" stop-color="var(--art-grey)"/>
          <stop offset="1" stop-color="var(--art-grey)"/>
        </linearGradient>
        <radialGradient id="sealGold" cx="0.35" cy="0.35" r="0.8">
          <stop offset="0" stop-color="var(--seal-gold-light)"/>
          <stop offset="0.6" stop-color="var(--seal-gold)"/>
          <stop offset="1" stop-color="#b9772c"/>
        </radialGradient>
      </defs>

      <!-- author band -->
      <rect class="author-band" x="0" y="0" width="896" height="104" fill="url(#redBand)"/>
      <rect class="author-rule" x="0" y="104" width="896" height="4" fill="var(--rule-gold)"/>
      <text class="author-name" x="448" y="78" text-anchor="middle" font-size="62" fill="#fff" textLength="420" lengthAdjust="spacingAndGlyphs">GODFREY T HASWELL</text>

      <!-- illustration area (behind lower title line) -->
      <rect class="cover-illustration" role="img" aria-label="Illustration of a dark grey heron-like figure with curling limbs and a glowing yellow light bulb as its head" x="240" y="400" width="412" height="400" rx="18" fill="url(#artTones)"/>

      <!-- title -->
      <text class="title-main" x="446" y="306" text-anchor="middle" font-size="212" fill="var(--brand-red)" textLength="548" lengthAdjust="spacingAndGlyphs">WALTZ</text>
      <text class="title-link" x="448" y="370" text-anchor="middle" font-size="62" fill="url(#darkInk)" textLength="240" lengthAdjust="spacingAndGlyphs">BESIDE A</text>
      <text class="title-main" x="448" y="538" text-anchor="middle" font-size="178" fill="var(--brand-red)" textLength="696" lengthAdjust="spacingAndGlyphs">HERON</text>

      <!-- lower panel -->
      <rect class="tagline-panel" x="0" y="808" width="896" height="352" fill="var(--panel-grey)"/>

      <g class="tagline">
        <text x="86" y="900" font-size="82" textLength="474" lengthAdjust="spacingAndGlyphs"><tspan fill="var(--brand-red)">HOW</tspan><tspan fill="var(--brand-red)" font-size="48">TO</tspan><tspan fill="url(#darkInk)">BUILD</tspan></text>
        <text x="86" y="982" font-size="92" fill="var(--brand-red)" textLength="474" lengthAdjust="spacingAndGlyphs">MOTIVATION</text>
        <text x="86" y="1028" font-size="52" textLength="474" lengthAdjust="spacingAndGlyphs"><tspan fill="url(#darkInk)" font-size="38">AND </tspan><tspan fill="var(--brand-red)">OWNERSHIP</tspan></text>
        <text x="86" y="1078" font-size="54" fill="url(#darkInk)" textLength="474" lengthAdjust="spacingAndGlyphs">THROUGH FIVE PIVOTAL</text>
        <text x="86" y="1122" font-size="54" fill="var(--brand-red)" textLength="474" lengthAdjust="spacingAndGlyphs">MENTORING MOMENTS</text>
      </g>

      <!-- seal -->
      <g class="seal">
        <circle cx="720" cy="980" r="144" fill="url(#sealGold)"/>
        <circle cx="720" cy="980" r="120" fill="var(--seal-navy)"/>
        <circle cx="720" cy="980" r="106" fill="url(#sealGold)"/>
        <text class="seal-text" x="720" y="936" text-anchor="middle" font-size="40" fill="var(--seal-navy)" textLength="124" lengthAdjust="spacingAndGlyphs">A MAP FOR</text>
        <text class="seal-text" x="720" y="982" text-anchor="middle" font-size="40" fill="var(--seal-navy)" textLength="120" lengthAdjust="spacingAndGlyphs">HONEST</text>
        <text class="seal-text" x="720" y="1032" text-anchor="middle" font-size="40" fill="var(--seal-navy)" textLength="160" lengthAdjust="spacingAndGlyphs">MENTORING</text>
        <line x1="682" y1="1054" x2="758" y2="1054" stroke="var(--seal-navy)" stroke-width="2"/>
        <line x1="694" y1="1064" x2="746" y2="1064" stroke="var(--seal-navy)" stroke-width="2"/>
      </g>
    </svg>
  </div>
</div>
</body>
</html>
```